New local Orchid nursery branding

We need a business card designed for our small local company in Darwin, Australia that grows orchids, called Blooms at Carrow.
We will be running private sales from our property, and handing these out at local events for perspective customers.

We would like to see designs that are simple, and able to be used with minimal colours and containing an orchid, preferably a stylised representation instead of a photo.
The eventual hope is to take this into larger formats to create our company logo/branding etc, but for now we just need business cards.

Target Market(s)

Local Orchid

Industry/Entity Type

Business

Contact Information for Business Card

Company Name
Logo
Name
Phone Number
Street Address
Email Address (less prominent than rest of the text)

Font styles to use
Sans Serif

Requirements
Must have
• Name of the company, which is Blooms at Carrow
Nice to have
• stylised orchid logo
Should not have
• too many colours

```html
<!DOCTYPE html>
<html lang="en">
<head>
<meta charset="utf-8">
<title>Blooms at Carrow – Business Card</title>
<link rel="stylesheet" href="https://fonts.googleapis.com/css2?family=Open+Sans:wght@400;600;700&display=swap">
<style>
  :root {
    --page-bg: #ecebe8;
    --kraft-light: #cdab82;
    --kraft-dark: #b8946a;
    --ink: #141210;
    --shadow: rgba(60, 40, 20, 0.25);
  }
  * { margin: 0; padding: 0; box-sizing: border-box; }
  html, body {
    width: 1200px;
    height: 900px;
    overflow: hidden;
    background: var(--page-bg);
    font-family: "Open Sans", Arial, sans-serif;
    color: var(--ink);
  }
  .canvas {
    position: relative;
    width: 1200px;
    height: 900px;
  }
  .card {
    position: absolute;
    width: 556px;
    height: 342px;
    overflow: hidden;
    background: linear-gradient(135deg, var(--kraft-light) 0%, var(--kraft-dark) 100%);
    box-shadow: 0 6px 18px var(--shadow);
  }
  .card--front { left: 238px; top: 62px; }
  .card--back  { left: 458px; top: 518px; }

  /* front */
  .front__accent {
    position: absolute;
    left: -110px;
    top: 100px;
    width: 300px;
    height: 300px;
    border-radius: 50%;
    background: var(--ink);
  }
  .front__company {
    position: absolute;
    left: 212px;
    top: 70px;
    font-size: 32px;
    font-weight: 400;
    letter-spacing: 0.5px;
    white-space: nowrap;
  }
  .front__person {
    position: absolute;
    left: 212px;
    top: 150px;
    font-size: 18px;
    font-weight: 700;
  }
  .front__contacts {
    position: absolute;
    left: 212px;
    top: 186px;
    list-style: none;
    font-size: 14.5px;
    line-height: 20px;
  }
  .front__contacts li { display: flex; align-items: center; gap: 6px; }
  .front__contacts .contact--email { font-size: 14px; }
  .front__contacts svg { width: 12px; height: 12px; fill: var(--ink); }
  .front__address {
    position: absolute;
    left: 212px;
    top: 243px;
    font-size: 14.5px;
    line-height: 19px;
    font-style: normal;
  }

  /* back */
  .back__mark {
    position: absolute;
    left: 243px;
    top: 92px;
    width: 80px;
    height: 80px;
    background: var(--ink);
  }
  .back__company {
    position: absolute;
    left: 0;
    right: 0;
    top: 206px;
    text-align: center;
    font-size: 38px;
    font-weight: 400;
    letter-spacing: 0.5px;
  }
</style>
</head>
<body>
<main class="canvas">
  <section class="card card--front" aria-label="Business card front">
    <div class="front__accent"></div>
    <h1 class="front__company">Blooms at Carrow</h1>
    <p class="front__person">Daniel Reeves</p>
    <ul class="front__contacts">
      <li class="contact--phone">
        <svg viewBox="0 0 24 24" aria-hidden="true"><path d="M6.6 10.8a15.1 15.1 0 0 0 6.6 6.6l2.2-2.2a1 1 0 0 1 1-.25 11.4 11.4 0 0 0 3.6.57 1 1 0 0 1 1 1V20a1 1 0 0 1-1 1A17 17 0 0 1 3 4a1 1 0 0 1 1-1h3.5a1 1 0 0 1 1 1c0 1.25.2 2.45.57 3.57a1 1 0 0 1-.25 1z"/></svg>
        044-987 654 321
      </li>
      <li class="contact--email">
        <svg viewBox="0 0 24 24" aria-hidden="true"><path d="M2 5h20v14H2z M2 5l10 8 10-8" /></svg>
        hello@bloomsmail.com
      </li>
    </ul>
    <address class="front__address">12345, Address Goes Here<br>Country Name, 123456.</address>
  </section>

  <section class="card card--back" aria-label="Business card back">
    <div class="back__mark"></div>
    <h2 class="back__company">Blooms at Carrow</h2>
  </section>
</main>
</body>
</html>
```